Torvin Solutions

One page ad for conference program
We offer Cyber-Security, IT support, and VOIP.
We specialize in the Medical Industry
https://www.torvinsolutions.com

```html
<!DOCTYPE html>
<html lang="en">
<head>
<meta charset="UTF-8">
<title>Torvin Solutions – Conference Program Ad</title>
<link rel="stylesheet" href="https://fonts.googleapis.com/css2?family=Montserrat:ital,wght@0,500;0,600;0,700;0,800;1,700&family=Oswald:wght@600&display=swap">
<style>
  :root {
    --navy: #0f3f7c;
    --navy-deep: #0b2f5e;
    --orange: #e67b22;
    --ink: #1d1d1f;
    --grey: #8a8a8a;
    --paper: #f6f7f9;
    --white: #ffffff;
  }
  * { box-sizing: border-box; margin: 0; padding: 0; }
  html, body { width: 990px; height: 1200px; overflow: hidden; }
  body {
    background: var(--paper);
    font-family: "Montserrat", Arial, sans-serif;
    color: var(--ink);
    position: relative;
  }
  .ad { position: absolute; inset: 0; overflow: hidden;
    background: linear-gradient(180deg, #eef0f4 0%, #f7f8fa 45%, #f2f3f5 100%); }

  .hero-photo {
    position: absolute; left: 420px; top: 0; width: 570px; height: 566px;
    background:
      linear-gradient(90deg, rgba(238,240,244,1) 0%, rgba(238,240,244,0) 28%),
      linear-gradient(160deg, #aab6c7 0%, #4c6a94 40%, #1d3c6b 75%, #12294d 100%);
  }

  .brand { position: absolute; left: 98px; top: 92px; display: flex; align-items: center; gap: 14px; }
  .brand-mark { width: 22px; height: 22px; background: var(--navy); }
  .brand-name { font-weight: 800; font-size: 50px; color: var(--navy); letter-spacing: -1px; line-height: 1; }

  .offer { position: absolute; left: 98px; top: 262px; }
  .offer-lead { font-weight: 700; font-style: italic; font-size: 34px; color: #2a2a2a; margin-bottom: 6px; }
  .offer-line { font-family: "Oswald", "Arial Narrow", sans-serif; font-weight: 600;
    font-size: 56px; line-height: 67px; color: var(--navy); letter-spacing: 0.5px; }

  .specialty {
    position: absolute; left: 96px; top: 540px; width: 797px; height: 140px;
    background: var(--navy); color: var(--white);
    border-radius: 24px 0 24px 0; text-align: center;
    box-shadow: 0 14px 18px -12px rgba(0,0,0,0.35);
    padding-top: 18px;
  }
  .specialty-kicker { font-weight: 700; font-size: 30px; letter-spacing: 0.5px; }
  .specialty-title { font-weight: 800; font-size: 47px; line-height: 54px; }

  .services-tag {
    position: absolute; left: 308px; top: 720px; width: 375px; height: 51px;
    background: var(--orange); clip-path: polygon(8% 0, 100% 0, 92% 100%, 0 100%);
    color: var(--white); font-weight: 700; font-size: 30px;
    display: flex; align-items: center; justify-content: center;
  }

  .services { position: absolute; left: 0; top: 800px; width: 990px; height: 141px; }
  .service { position: absolute; top: 0; width: 150px; margin-left: -75px; text-align: center; }
  .service-icon {
    width: 64px; height: 64px; border-radius: 50%; background: var(--navy);
    margin: 1px auto 0; display: flex; align-items: center; justify-content: center;
    box-shadow: -10px 8px 14px rgba(0,0,0,0.12);
  }
  .service-icon svg { width: 36px; height: 36px; }
  .service-label { margin-top: 22px; font-weight: 700; font-size: 16.5px; line-height: 22px; color: #222; }
  .divider { position: absolute; top: 0; width: 2px; height: 141px; background: var(--navy); }

  .tagline { position: absolute; left: 0; width: 990px; top: 962px; text-align: center;
    font-weight: 800; font-size: 25px; color: var(--ink); }
  .tagline-accent { color: var(--navy); }

  .call-band { position: absolute; left: 0; top: 1014px; width: 990px; height: 80px;
    background: var(--orange); color: var(--white); font-weight: 800; font-size: 45px;
    display: flex; align-items: center; justify-content: center; letter-spacing: 0.3px; }

  .contact-band { position: absolute; left: 0; top: 1094px; width: 990px; height: 46px;
    background: var(--navy); color: var(--white); font-weight: 500; font-size: 20px;
    display: flex; align-items: center; justify-content: center; gap: 28px; }
  .contact-item { display: flex; align-items: center; gap: 10px; }
  .contact-item svg { width: 18px; height: 18px; }

  .coverage { position: absolute; left: 0; width: 990px; top: 1150px; text-align: center;
    font-weight: 500; font-size: 16.5px; color: #222; }
</style>
</head>
<body>
<main class="ad">
  <div class="hero-photo" role="img" aria-label="Photo of a businessman in a suit touching a glowing network diagram of cloud, email, device and server icons over a city skyline"></div>

  <header class="brand">
    <span class="brand-mark"></span>
    <span class="brand-name">Torvin Solutions</span>
  </header>

  <section class="offer">
    <p class="offer-lead">We offer</p>
    <p class="offer-line">CYBER-SECURITY</p>
    <p class="offer-line">IT SUPPORT</p>
    <p class="offer-line">AND VOIP</p>
  </section>

  <section class="specialty">
    <p class="specialty-kicker">WE SPECIALIZE IN THE</p>
    <p class="specialty-title">MEDICAL INDUSTRY</p>
  </section>

  <div class="services-tag">OUR SERVICES</div>

  <section class="services">
    <div class="service" style="left:158px">
      <div class="service-icon"><svg viewBox="0 0 36 36" fill="none" stroke="#fff" stroke-width="1.8"><rect x="7" y="9" width="22" height="15" rx="1.5"/><path d="M4 27h28"/><circle cx="18" cy="16.5" r="3.5"/></svg></div>
      <p class="service-label">Managed<br>IT Services</p>
    </div>
    <div class="divider" style="left:245px"></div>
    <div class="service" style="left:319px">
      <div class="service-icon"><svg viewBox="0 0 36 36" fill="none" stroke="#fff" stroke-width="1.8"><rect x="6" y="8" width="24" height="16" rx="1.5"/><path d="M18 28v-4M12 29h12"/><path d="M18 11l4 1.5v3c0 3-2 4.5-4 5.5-2-1-4-2.5-4-5.5v-3z"/></svg></div>
      <p class="service-label">Cyber<br>Security</p>
    </div>
    <div class="divider" style="left:394px"></div>
    <div class="service" style="left:494px">
      <div class="service-icon"><svg viewBox="0 0 36 36" fill="none" stroke="#fff" stroke-width="1.8"><rect x="7" y="9" width="22" height="15" rx="1.5"/><path d="M4 27h28"/><path d="M18 12.5l4 2v4l-4 2-4-2v-4z"/></svg></div>
      <p class="service-label">Virtualization</p>
    </div>
    <div class="divider" style="left:594px"></div>
    <div class="service" style="left:674px">
      <div class="service-icon"><svg viewBox="0 0 36 36" fill="none" stroke="#fff" stroke-width="1.8"><path d="M9 10c-2 3 0 9 5 14s11 7 14 5l-1-4-4-1-2 2c-3-1-6-4-7-7l2-2-1-4z"/><path d="M21 8a7 7 0 0 1 7 7M21 12a3 3 0 0 1 3 3"/></svg></div>
      <p class="service-label">VoIP<br>Solutions</p>
    </div>
    <div class="divider" style="left:755px"></div>
    <div class="service" style="left:834px">
      <div class="service-icon"><svg viewBox="0 0 36 36" fill="none" stroke="#fff" stroke-width="1.8"><rect x="9" y="6" width="18" height="7" rx="1"/><rect x="9" y="14.5" width="18" height="7" rx="1"/><rect x="9" y="23" width="18" height="7" rx="1"/><path d="M12 9.5h2M12 18h2M12 26.5h2"/></svg></div>
      <p class="service-label">Hosted<br>Solutions</p>
    </div>
  </section>

  <p class="tagline"><span class="tagline-accent">EXPERIENCE IT SUPPORT</span> THE WAY IT SHOULD BE</p>

  <div class="call-band">CALL US TODAY: 813-555-0147</div>

  <div class="contact-band">
    <span class="contact-item"><svg viewBox="0 0 18 18" fill="none" stroke="#e67b22" stroke-width="1.4"><rect x="2" y="4" width="14" height="10"/><path d="M2 4l7 6 7-6"/></svg>contact@torvinsolutions.com</span>
    <span>|</span>
    <span class="contact-item"><svg viewBox="0 0 18 18" fill="none" stroke="#e67b22" stroke-width="1.4"><circle cx="9" cy="9" r="7"/><ellipse cx="9" cy="9" rx="3" ry="7"/><path d="M2 9h14"/></svg>www.TorvinSolutions.com</span>
  </div>

  <p class="coverage">IT Services &amp; Support Covering Tampa, St Pete, Sarasota, Ft Myers, and Naples</p>
</main>
</body>
</html>
```